Billboard For Marek Delvaine

Need a Billboard 8ft. High x 16ft. Long. Ive attached a former billboard and looking for the same thing just updated with:
Summit Lodge Award Logo - 2020, 2022
Pinnacle Ring award Logo - 2022

Thanks.

```html
<!DOCTYPE html>
<html lang="en">
<head>
<meta charset="utf-8">
<title>Billboard – Marek Delvaine</title>
<link href="https://fonts.googleapis.com/css2?family=Oswald:wght@300;400;600;700&family=Poppins:wght@600;700;800&display=swap" rel="stylesheet">
<style>
  :root {
    --red: #d4121f;
    --black: #0d0d0d;
    --white: #ffffff;
    --stage: #3d3d3d;
    --photo-blue: #3a5fb0;
    --photo-light: #e9eef6;
  }
  * { box-sizing: border-box; margin: 0; padding: 0; }
  html, body { width: 720px; height: 1200px; overflow: hidden; }
  body { background: var(--stage); position: relative; }

  .billboard {
    position: absolute; left: 20px; top: 430px;
    width: 680px; height: 340px;
    background: var(--white); overflow: hidden;
    box-shadow: 0 4px 14px rgba(0,0,0,.45);
  }
  .headline {
    position: absolute; left: 27px; top: 12px;
    font-family: "Oswald", sans-serif; font-weight: 600;
    font-size: 56px; line-height: 64px; letter-spacing: .5px;
    color: var(--black); white-space: nowrap;
  }
  .headline .accent { color: var(--red); }

  .name-band {
    position: absolute; left: 0; top: 87px; width: 680px; height: 77px;
    background: var(--black);
  }
  .agent-name {
    position: absolute; left: 52px; top: 94px;
    font-family: "Poppins", sans-serif; font-weight: 700;
    font-size: 36px; line-height: 42px; color: var(--white); letter-spacing: 1px;
  }
  .agent-title {
    position: absolute; left: 61px; top: 136px;
    font-family: "Poppins", sans-serif; font-weight: 600;
    font-size: 17px; line-height: 20px; color: var(--white); letter-spacing: 7.5px;
  }

  .phone {
    position: absolute; left: 42px; top: 164px; height: 66px;
    display: flex; align-items: center; gap: 8px;
  }
  .phone-number {
    font-family: "Poppins", sans-serif; font-weight: 800;
    font-size: 48px; line-height: 1; color: var(--red); letter-spacing: 1px;
  }

  .values-band {
    position: absolute; left: 0; top: 231px; width: 500px; height: 33px;
    background: var(--red);
    clip-path: polygon(0 0, 100% 0, 97% 100%, 0 100%);
  }
  .values {
    position: absolute; left: 52px; top: 231px; height: 33px;
    display: flex; align-items: center; gap: 14px;
    font-family: "Oswald", sans-serif; font-weight: 600;
    font-size: 25px; color: var(--white);
  }
  .value { display: flex; align-items: center; gap: 4px; }

  .agent-photo {
    position: absolute; left: 480px; top: 78px; width: 200px; height: 186px;
    background: linear-gradient(180deg, var(--photo-light) 0%, #b9c6de 45%, var(--photo-blue) 100%);
    clip-path: polygon(18% 0, 100% 0, 100% 100%, 0 100%, 4% 62%);
  }

  .footer {
    position: absolute; left: 0; top: 264px; width: 680px; height: 76px;
  }
  .award { position: absolute; display: flex; align-items: center; gap: 5px; color: var(--black); }
  .award-seal { flex: none; }
  .award-text { font-family: "Oswald", sans-serif; font-weight: 300; line-height: 1; }
  .award-issuer { font-family: "Poppins", sans-serif; font-weight: 600; font-size: 7px; letter-spacing: .3px; margin-bottom: 2px; }
  .award-name { font-size: 17px; }
  .award-name.strong { font-weight: 400; font-size: 16px; }
  .award-note { font-family: "Poppins", sans-serif; font-size: 6px; font-weight: 600; line-height: 1.1; border-left: 1px solid var(--black); padding-left: 3px; margin-left: 4px; }
  .award-line { display: flex; align-items: center; }
  .award-years { font-weight: 400; font-size: 11px; margin-top: 2px; letter-spacing: .3px; }

  .award-pinnacle { left: 42px; top: 12px; }
  .award-summit { left: 206px; top: 6px; }

  .brokerage {
    position: absolute; left: 378px; top: 26px;
    display: flex; align-items: center; gap: 7px;
    font-family: "Poppins", sans-serif; font-weight: 800;
    font-size: 16px; line-height: 22px; color: var(--black); letter-spacing: .5px;
    white-space: nowrap;
  }
  .brokerage-mark { width: 22px; height: 22px; background: var(--red); flex: none; }

  .social { position: absolute; left: 580px; top: 20px; display: flex; flex-direction: column; gap: 6px; }
  .social-link {
    display: flex; align-items: center; gap: 5px;
    font-family: "Poppins", sans-serif; font-weight: 700; font-size: 12px; line-height: 14px; color: var(--red);
  }
  .social-mark { width: 12px; height: 12px; background: var(--red); border-radius: 3px; flex: none; }
</style>
</head>
<body>
  <main class="billboard">
    <h1 class="headline"><span class="accent">BUYING</span> OR <span class="accent">SELLING?</span> CALL</h1>

    <div class="name-band"></div>
    <p class="agent-name">MAREK DELVAINE</p>
    <p class="agent-title">SALES REPRESENTATIVE</p>

    <div class="agent-photo" role="img" aria-label="Portrait photo of the agent in a blue shirt and tie"></div>

    <div class="phone">
      <svg width="30" height="30" viewBox="0 0 24 24" aria-hidden="true">
        <path d="M6.6 10.8c1.4 2.8 3.8 5.1 6.6 6.6l2.2-2.2c.3-.3.7-.4 1-.2 1.1.4 2.3.6 3.6.6.6 0 1 .4 1 1V20c0 .6-.4 1-1 1C10.6 21 3 13.4 3 4c0-.6.4-1 1-1h3.5c.6 0 1 .4 1 1 0 1.3.2 2.5.6 3.6.1.3 0 .7-.2 1L6.6 10.8z" fill="var(--red)"/>
        <path d="M14.5 3.5a6 6 0 0 1 6 6M14.5 6.5a3 3 0 0 1 3 3" stroke="var(--red)" stroke-width="1.8" fill="none" stroke-linecap="round"/>
      </svg>
      <span class="phone-number">613.555.0174</span>
    </div>

    <div class="values-band"></div>
    <div class="values">
      <span class="value">
        <svg width="13" height="13" viewBox="0 0 16 16" aria-hidden="true"><circle cx="8" cy="8" r="8" fill="var(--black)"/><path d="M4.5 8.2l2.3 2.3 4.7-4.8" stroke="var(--red)" stroke-width="2" fill="none"/></svg>
        FOCUSED
      </span>
      <span class="value">
        <svg width="13" height="13" viewBox="0 0 16 16" aria-hidden="true"><circle cx="8" cy="8" r="8" fill="var(--black)"/><path d="M4.5 8.2l2.3 2.3 4.7-4.8" stroke="var(--red)" stroke-width="2" fill="none"/></svg>
        DRIVEN
      </span>
      <span class="value">
        <svg width="13" height="13" viewBox="0 0 16 16" aria-hidden="true"><circle cx="8" cy="8" r="8" fill="var(--black)"/><path d="M4.5 8.2l2.3 2.3 4.7-4.8" stroke="var(--red)" stroke-width="2" fill="none"/></svg>
        EXPERIENCED!
      </span>
    </div>

    <footer class="footer">
      <div class="award award-pinnacle">
        <svg class="award-seal" width="34" height="34" viewBox="0 0 34 34" aria-hidden="true"><circle cx="17" cy="17" r="16" fill="var(--black)"/></svg>
        <div class="award-text">
          <p class="award-issuer">CROWN HEARTH</p>
          <p class="award-name">PINNACLE RING</p>
          <p class="award-name">AWARD 2022</p>
        </div>
      </div>

      <div class="award award-summit">
        <svg class="award-seal" width="48" height="48" viewBox="0 0 48 48" aria-hidden="true"><circle cx="24" cy="24" r="23" fill="none" stroke="var(--black)" stroke-width="1.2"/><circle cx="24" cy="24" r="16" fill="var(--black)"/></svg>
        <div class="award-text">
          <p class="award-issuer">CROWN HEARTH</p>
          <p class="award-name strong">SUMMIT</p>
          <div class="award-line"><p class="award-name strong">LODGE</p><p class="award-note">NATIONAL<br>TOP 1%</p></div>
          <p class="award-years">2020 · 2022</p>
        </div>
      </div>

      <div class="brokerage"><span class="brokerage-mark"></span>CROWN HEARTH</div>

      <div class="social">
        <span class="social-link"><span class="social-mark"></span>PIXSHARE</span>
        <span class="social-link"><span class="social-mark"></span>LINKBOOK</span>
      </div>
    </footer>
  </main>
</body>
</html>
```